2 stickers business card size and car sticker

design stickers for a 1300 phone number. 1 x 90mm x 42mm and the other 190mm x 50mm

The smaller art 90x42 will also be used for web and print the larger 190mm x 50mm will be used for print on a car bumper sticker. All final submissions should be original full photoshop files or illustrator files and include any font required.

The aim is to promote a 1300 phone number: 1300TANBERG

1300TANBERG should be the main attention grabber but also the actual phone number should also appear in small 1300 482 615

There can also be a secondary main attention word or words: CALL or CALL NOW and the web site 1300TANBERG.COM

You may also include a graphic such as a phone or other icon type graphic.

The small stickers 90x42 are to remind people of the number that will be stuck on desks, books, computers etc and also the bumper sticker.

2 examples of a smaller sticker are attached and are named example1 and example 2 .. but do not represent any style guide just a rough example of the type of ideas we are aiming for .. different ideas welcomed. I have also uploaded a bit of a fun graphic called "freefall_person" if people want to try a bit of a fun car bumper sticker design , I am open to other graphic elements .. this is just one and would fit in with part B of the brief below. If your designing a part A sticker then you would use the icon graphic or parts of the icon graphic for part B

We have a current brand that is represented by the blue and back icon with the white man and the word SKYDIVE We are looking for two styles of design submissions:

A) Designs that promote the new 1300TANBERG but also tie in with the current brand either with colour alone or by incorporating the icon graphic or both.

B) Designs that simply promote 1300TANBERG and have no tie to the current brand.

Submissions can target either A or B but those that contain designs for both A and B will be looked on more favourably.

```html
<!DOCTYPE html>
<html lang="en">
<head>
<meta charset="utf-8">
<title>1300TANBERG Stickers</title>
<link rel="stylesheet" href="https://fonts.googleapis.com/css2?family=PT+Sans:wght@400;700&family=Arimo:wght@400&display=swap">
<style>
  :root {
    --sticker-black: #000000;
    --brand-blue: #1ba3e2;
    --tab-grey: #8a8a8a;
    --frame-grey: #7d7d7d;
    --white: #ffffff;
    --page: #ffffff;
    --band-light: #c9c9c7;
    --band-dark: #9d9d9b;
  }
  * { box-sizing: border-box; margin: 0; padding: 0; }
  html, body { width: 1200px; height: 900px; overflow: hidden; background: var(--page); }
  .board { position: relative; width: 1200px; height: 900px; }

  .sticker {
    position: absolute;
    background: var(--sticker-black);
    overflow: hidden;
    font-family: "PT Sans", sans-serif;
    color: var(--white);
  }
  .sticker--grey { border: 3px solid var(--frame-grey); border-radius: 7px; }
  .sticker--blue { border: 3px solid var(--brand-blue); border-radius: 9px; }

  .web-tab {
    position: absolute;
    top: 0;
    right: 0;
    font-family: "Arimo", sans-serif;
    white-space: nowrap;
    display: flex;
    align-items: center;
  }
  .web-tab--grey { background: var(--tab-grey); color: var(--white); border-bottom-left-radius: 6px; }
  .web-tab--blue { background: var(--brand-blue); color: var(--sticker-black); border-radius: 0 0 6px 6px; }
  .cursor { position: absolute; }

  .call-now { position: absolute; color: var(--brand-blue); font-weight: 700; white-space: nowrap; line-height: 1; }
  .phone { position: absolute; font-family: "Arimo", sans-serif; white-space: nowrap; line-height: 1; }
  .number-name { position: absolute; font-weight: 700; white-space: nowrap; line-height: 1; letter-spacing: -0.5px; }
  .brand-dot { position: absolute; background: var(--brand-blue); border-radius: 50%; }

  .vehicle-preview {
    position: absolute; left: 656px; top: 0; width: 544px; height: 788px;
    background: linear-gradient(180deg, #f4f4f4 0%, #e6e6e6 60%, #f6f6f6 100%);
  }
  .footer-band {
    position: absolute; left: 0; top: 788px; width: 1200px; height: 112px;
    background: linear-gradient(90deg, var(--band-light), var(--band-dark) 50%, var(--band-light));
  }
</style>
</head>
<body>
<main class="board">

  <!-- Small sticker with brand dot -->
  <section class="sticker sticker--grey" style="left:40px;top:100px;width:277px;height:128px;">
    <div class="brand-dot" style="left:8px;top:6px;width:80px;height:80px;"></div>
    <div class="web-tab web-tab--grey" style="width:160px;height:29px;padding-left:7px;font-size:13px;">www.1300tanberg.com</div>
    <svg class="cursor" style="left:228px;top:17px;" width="12" height="16" viewBox="0 0 12 16"><path d="M1 1 L1 13 L4 10 L6.5 15 L8.5 14 L6 9 L10 9 Z" fill="#fff" stroke="#000" stroke-width="1"/></svg>
    <div class="call-now" style="left:109px;top:36px;font-size:30px;">CALL NOW</div>
    <div class="phone" style="left:168px;top:66px;font-size:12px;">1300 482 615</div>
    <div class="number-name" style="left:12px;top:83px;font-size:37px;">1300TANBERG</div>
  </section>

  <!-- Small sticker, text only -->
  <section class="sticker sticker--grey" style="left:349px;top:100px;width:277px;height:128px;">
    <div class="web-tab web-tab--grey" style="width:160px;height:29px;padding-left:7px;font-size:13px;">www.1300tanberg.com</div>
    <svg class="cursor" style="left:228px;top:17px;" width="12" height="16" viewBox="0 0 12 16"><path d="M1 1 L1 13 L4 10 L6.5 15 L8.5 14 L6 9 L10 9 Z" fill="#fff" stroke="#000" stroke-width="1"/></svg>
    <div class="call-now" style="left:10px;top:40px;font-size:31px;">CALL NOW</div>
    <div class="phone" style="left:181px;top:56px;font-size:12px;">1300 482 615</div>
    <div class="number-name" style="left:10px;top:74px;font-size:40px;">1300TANBERG</div>
  </section>

  <!-- Bumper sticker, text only -->
  <section class="sticker sticker--blue" style="left:52px;top:363px;width:550px;height:144px;">
    <div class="web-tab web-tab--blue" style="width:211px;height:38px;padding-left:8px;font-size:17px;">www.1300tanberg.com</div>
    <svg class="cursor" style="left:484px;top:24px;" width="15" height="20" viewBox="0 0 12 16"><path d="M1 1 L1 13 L4 10 L6.5 15 L8.5 14 L6 9 L10 9 Z" fill="#fff" stroke="#000" stroke-width="1"/></svg>
    <div class="call-now" style="left:17px;top:13px;font-size:34px;">CALL NOW</div>
    <div class="phone" style="left:182px;top:26px;font-size:18px;">(1300 482 615)</div>
    <div class="number-name" style="left:13px;top:49px;font-size:82px;letter-spacing:-1px;">1300TANBERG</div>
  </section>

  <!-- Bumper sticker with brand dot -->
  <section class="sticker sticker--blue" style="left:52px;top:581px;width:550px;height:144px;">
    <div class="web-tab web-tab--blue" style="right:auto;left:185px;width:212px;height:38px;padding-left:9px;font-size:17px;">www.1300tanberg.com</div>
    <svg class="cursor" style="left:337px;top:26px;" width="15" height="20" viewBox="0 0 12 16"><path d="M1 1 L1 13 L4 10 L6.5 15 L8.5 14 L6 9 L10 9 Z" fill="#fff" stroke="#000" stroke-width="1"/></svg>
    <div class="call-now" style="left:17px;top:12px;font-size:34px;">CALL NOW</div>
    <div class="phone" style="left:19px;top:49px;font-size:22px;">1300 482 615</div>
    <div class="number-name" style="left:13px;top:74px;font-size:59px;">1300TANBERG</div>
    <div class="brand-dot" style="left:428px;top:32px;width:96px;height:96px;"></div>
  </section>

  <div class="vehicle-preview" role="img" aria-label="Photo of a white SUV rear with the bumper sticker applied"></div>
  <div class="footer-band" role="img" aria-label="Grey textured concrete band"></div>

</main>
</body>
</html>
```